Professional business podcast cover

Hey guys,

I want to redesign my podcast cover from the Velmo Podcast.

It is a professional business podcast for small and medium sized business. Therefor I need something professional.
No fancy glitter designs.
Something real clean and easy.

I am thinking about something similar to this pic.
https://pinsa.example/7Qk4m2Rt91Xe

What is important for the design?

1. professional and clean look
2. fonts= roboto
3. the logo must be readable also on small devices (please do not change the existing logo!)
4. same color as the logo
5. my full name must be included in the design: Tiro Basko

Thank you for your work.

I can not wait to get your designs.

Regards

Tiro from Velmo

Reason: I need a perfect fitting timeless design. If it needs more time to be generated, than we do so.

Target Market(s)

Small and medium sized CEOs

Industry/Entity Type

Consulting

Font styles to use
Sans Serif

Colors
acd136

Requirements
Must have
• 1. professional and clean look
• 2. fonts= roboto
• 3. the logo must be readable also on small devices
• 4. same color as the logo
• 5. size 1400x 1400
• 6. Text: Tiro Basko very present
Nice to have
• Get inspired by covers like Jon Melder, Gary Hollis or Ned Crowles podcast.
• https://pinsa.example/5vB8n3Lw2Yq0
• https://pinsa.example/9Hd6p1Ks4Ua7
• https://pinsa.example/3Fg2x8Mj6Ce5
Should not have
• Fancy glossi shinny designs

```html
<!DOCTYPE html>
<html lang="de">
<head>
<meta charset="utf-8">
<title>Velmo Podcast – Tiro Basko</title>
<link rel="stylesheet" href="https://fonts.googleapis.com/css2?family=Roboto:wght@400;500&display=swap">
<style>
  :root {
    --brand-green: #2fb44a;
    --ink: #3a3a3c;
    --rule: #3d3d40;
    --bg-light: #fbf9ef;
    --bg-mid: #d9d8cf;
    --bg-dark: #9fa19c;
    --portrait-top: #d7c9b8;
    --portrait-mid: #c9b7a5;
    --portrait-suit: #1c2233;
  }
  html, body {
    margin: 0;
    padding: 0;
    width: 1200px;
    height: 1199px;
    overflow: hidden;
    background: #ffffff;
  }
  .cover {
    position: relative;
    width: 1200px;
    height: 1199px;
    overflow: hidden;
    font-family: "Roboto", Arial, sans-serif;
  }
  .backdrop {
    position: absolute;
    inset: 0;
    background:
      radial-gradient(ellipse 700px 600px at 15% 15%, var(--bg-light) 0%, rgba(251,249,239,0) 70%),
      linear-gradient(100deg, var(--bg-light) 0%, var(--bg-mid) 45%, var(--bg-dark) 100%);
  }
  .portrait {
    position: absolute;
    left: 660px;
    top: 170px;
    width: 540px;
    height: 1029px;
    border-radius: 240px 240px 0 0;
    background: linear-gradient(180deg, var(--portrait-top) 0%, var(--portrait-mid) 45%, #e8e8ea 62%, var(--portrait-suit) 72%, var(--portrait-suit) 100%);
  }
  .brand {
    position: absolute;
    left: 122px;
    top: 150px;
    margin: 0;
    font-size: 190px;
    font-weight: 500;
    line-height: 1;
    letter-spacing: 2px;
    color: var(--brand-green);
  }
  .divider {
    position: absolute;
    left: 80px;
    top: 394px;
    width: 630px;
    height: 4px;
    background: var(--rule);
  }
  .host-name {
    position: absolute;
    left: 80px;
    top: 418px;
    width: 630px;
    margin: 0;
    text-align: center;
    font-size: 96px;
    font-weight: 400;
    line-height: 1.1;
    color: var(--ink);
  }
  .tagline {
    position: absolute;
    left: 80px;
    top: 578px;
    width: 630px;
    margin: 0;
    text-align: center;
    font-size: 41px;
    font-weight: 400;
    line-height: 1.25;
    color: var(--ink);
  }
</style>
</head>
<body>
  <main class="cover">
    <div class="backdrop" role="img" aria-label="Softly blurred bright office corridor background"></div>
    <div class="portrait" role="img" aria-label="Portrait photo of the host in a dark suit, white shirt and dark green tie"></div>
    <h1 class="brand">Velmo</h1>
    <div class="divider"></div>
    <h2 class="host-name">Tiro Basko</h2>
    <p class="tagline">Unternehmerwissen<br>in 15 Minuten</p>
  </main>
</body>
</html>
```